3 Posters for House Designer

I'm installing a set of 3 posters on our office wall to describe the benefits of our house design services. These posters are A0 size and will be seen from the front windows of the office. I have already purchased the AO snap frames to hold the posters, they are silver in colour.

We, Farlow Studio, design houses. We offer Architectural services but as we didn't study Architecture, we're not permitted to use the word Architect or any derivative there of. So no words allowed that say Architect, Architecture or Architectural and the like.

Each poster will highlight a benefit of engaging Farlow Studio to design a house and the posters will be lined up side by side.

The first benefit is GENUINE PASSION.
I am genuinely passionate about designing homes that fit my clients like a glove in every way. I genuinely care about my clients doing the right thing by themselves and I'm not a "yes man". I challenge myself and my clients to ensure the best possible result.

The second benefit is CREATIVE THINKING.
I love a challenge. I can spend hours, even days, working on one small aspect of a house design to make it work best. I love solving design problems on difficult sites. What I pride myself on is delivering house designs which are as great to live with as they are to look at; form and function, beautiful yet practical.

The third benefit is GUARANTEED RESULTS.
My genuine passion and creative thinking result in my initial house designs being 95% right, for my clients, the first time; requiring very few changes. This is why I offer, iron clad, guarantees which form part of our design contract. These guarantees include:
1. Our clients absolutely loving our design. If they want to change something, we'll change it at no additional cost; no matter how big the changes or how many.
2. We guarantee our house designs will be within the given budget to build the house. If not, we'll amend our design at no additional cost.
3. We guarantee our house designs will meet the required minimum 6 star energy efficiency rating. If not, we'll amend the design at no additional cost.
4. We guarantee Council approval to build as designed. If not, we'll amend our design at no additional cost.

I see each benefit title being the hero on each poster (ie GENUINE PASSION). I see white type on a light blue background. I see A hero shot of stylish houses in the backgrounds but blurred. I see life in the posters in the form of colour and happy people (customers). Our customers are aged between 40 & 60.

I have a logo (uploaded) and have already purchased images of people if required. Please advise if you want these.

Check out our website at www.farlow-studio.com.au/Kelmore

Target Market(s)

Couples aged 40 - 60

Industry/Entity Type

House

Requirements
Must have
• Stylish house images, happy people (couples & families), big, bold, hero titles at the top of each of the three posters.

```html
<!DOCTYPE html>
<html lang="en">
<head>
<meta charset="utf-8">
<title>Farlow Studio – Poster Series</title>
<link href="https://fonts.googleapis.com/css2?family=Anton&display=swap" rel="stylesheet">
<style>
  :root{
    --wall:#d3d3d3;
    --poster-blue:#2e3192;
    --frame:#f4f4f4;
    --brand-blue:#2b9ad6;
    --tagline:#1b1d5c;
  }
  html,body{margin:0;padding:0;overflow:hidden;}
  body{width:1200px;height:985px;background:var(--wall);position:relative;font-family:'Anton',sans-serif;}
  .poster{position:absolute;top:203px;width:387px;height:547px;background:var(--poster-blue);box-shadow:0 0 0 1px var(--frame);}
  .poster--passion{left:8px;}
  .poster--creative{left:407px;}
  .poster--results{left:805px;height:549px;}
  .poster svg{display:block;width:100%;height:100%;}
  .hero-word{font-family:'Anton',sans-serif;stroke:#ffffff;stroke-width:1;}
  .brand-name{font-family:'Anton',sans-serif;font-size:22px;fill:var(--brand-blue);letter-spacing:0.5px;}
  .brand-tagline{font-family:'Anton',sans-serif;font-size:6.5px;fill:var(--tagline);letter-spacing:0.6px;}
</style>
</head>
<body>

<section class="poster poster--passion">
  <svg viewBox="0 0 387 547" role="img" aria-label="Headline GENUINE PASSION with letters filled by a photo of a blue-trimmed house, a pool and a flowering garden">
    <defs>
      <linearGradient id="fill-passion" gradientUnits="userSpaceOnUse" x1="0" y1="25" x2="0" y2="460">
        <stop offset="0" stop-color="#d9e8f3"/>
        <stop offset="0.25" stop-color="#8ea6c4"/>
        <stop offset="0.5" stop-color="#a9b7c9"/>
        <stop offset="0.68" stop-color="#7fc0d8"/>
        <stop offset="0.82" stop-color="#8a9a5c"/>
        <stop offset="1" stop-color="#6d8a4e"/>
      </linearGradient>
    </defs>
    <text class="hero-word" fill="url(#fill-passion)" x="27" y="139" font-size="130" textLength="255" lengthAdjust="spacingAndGlyphs">GENU</text>
    <text class="hero-word" fill="url(#fill-passion)" x="27" y="269" font-size="128" textLength="153" lengthAdjust="spacingAndGlyphs">INE</text>
    <text class="hero-word" fill="url(#fill-passion)" x="27" y="459" font-size="192" textLength="337" lengthAdjust="spacingAndGlyphs">PASSION</text>
    <text class="brand-name" x="193" y="512" text-anchor="middle">farlow studio</text>
    <text class="brand-tagline" x="193" y="524" text-anchor="middle">RESIDENTIAL DESIGNERS PERTH WESTERN AUSTRALIA</text>
  </svg>
</section>

<section class="poster poster--creative">
  <svg viewBox="0 0 387 547" role="img" aria-label="Headline CREATIVE THINKING with letters filled by a photo of a white weatherboard house front and garden path">
    <defs>
      <linearGradient id="fill-creative" gradientUnits="userSpaceOnUse" x1="0" y1="25" x2="0" y2="460">
        <stop offset="0" stop-color="#b9c3c9"/>
        <stop offset="0.22" stop-color="#eef0ea"/>
        <stop offset="0.5" stop-color="#c8c8a8"/>
        <stop offset="0.7" stop-color="#b2b79a"/>
        <stop offset="0.85" stop-color="#a7b78d"/>
        <stop offset="1" stop-color="#e2e4e0"/>
      </linearGradient>
    </defs>
    <text class="hero-word" fill="url(#fill-creative)" x="27" y="139" font-size="130" textLength="256" lengthAdjust="spacingAndGlyphs">CREA</text>
    <text class="hero-word" fill="url(#fill-creative)" x="25" y="269" font-size="128" textLength="216" lengthAdjust="spacingAndGlyphs">TIVE</text>
    <text class="hero-word" fill="url(#fill-creative)" x="25" y="459" font-size="192" textLength="334" lengthAdjust="spacingAndGlyphs">THINKING</text>
    <text class="brand-name" x="193" y="512" text-anchor="middle">farlow studio</text>
    <text class="brand-tagline" x="193" y="524" text-anchor="middle">RESIDENTIAL DESIGNERS PERTH WESTERN AUSTRALIA</text>
  </svg>
</section>

<section class="poster poster--results">
  <svg viewBox="0 0 387 549" role="img" aria-label="Headline GUARANTEED RESULTS with letters filled by a photo of a smiling older couple in front of their house and picket fence">
    <defs>
      <linearGradient id="fill-results" gradientUnits="userSpaceOnUse" x1="0" y1="25" x2="387" y2="460">
        <stop offset="0" stop-color="#b8c4c0"/>
        <stop offset="0.3" stop-color="#7f9a6c"/>
        <stop offset="0.5" stop-color="#e9b8c8"/>
        <stop offset="0.7" stop-color="#9eb4dc"/>
        <stop offset="1" stop-color="#7f98c8"/>
      </linearGradient>
    </defs>
    <text class="hero-word" fill="url(#fill-results)" x="24" y="139" font-size="130" textLength="338" lengthAdjust="spacingAndGlyphs">GUARA</text>
    <text class="hero-word" fill="url(#fill-results)" x="24" y="269" font-size="128" textLength="300" lengthAdjust="spacingAndGlyphs">NTEED</text>
    <text class="hero-word" fill="url(#fill-results)" x="24" y="459" font-size="192" textLength="338" lengthAdjust="spacingAndGlyphs">RESULTS</text>
    <text class="brand-name" x="193" y="512" text-anchor="middle">farlow studio</text>
    <text class="brand-tagline" x="193" y="524" text-anchor="middle">RESIDENTIAL DESIGNERS PERTH WESTERN AUSTRALIA</text>
  </svg>
</section>

</body>
</html>
```